Hal's Remedies Business Card Design Project

I need a business card designed for my pharmacy Hal's Remedies. I would like just the logo on one side, maybe with black background and white lettering. The other side I would also like to include my logo which is attached. Also, please include my name and the following information:
Hal Norwick Owner/Pharm D.
Business address is 7163 N Birch Rd Sioux Falls, SD 57291.
Phone number is 605-318-6027 and fax # is 605-318-6031.
my email address is hal@halsremedies.example.
My website is www.halsremedies.example.
My business hours are Monday-Friday 8am-7 pm. Saturday 8am-12 pm. Sunday Closed.
I would like the design to include my logo colors, black, white, and neon green. Silver may be added as a highlight. Thanks.
Pharmacy
See above in product description

```html
<!DOCTYPE html>
<html lang="en">
<head>
<meta charset="utf-8">
<title>Hal's Remedies – Business Card</title>
<link href="https://fonts.googleapis.com/css2?family=Lato:wght@400;700;900&display=swap" rel="stylesheet">
<style>
  :root {
    --stage: #1b1b1b;
    --card-dark: #1f1d1e;
    --card-light: #f7f7f7;
    --ink: #1a1a1a;
    --ink-soft: #333333;
    --white: #f2f2f2;
    --neon: #8cc63f;
    --rule: #1a1a1a;
    --silver: #9a9a9a;
  }
  html, body {
    margin: 0;
    padding: 0;
    width: 1200px;
    height: 873px;
    overflow: hidden;
    background: var(--stage);
    font-family: "Lato", sans-serif;
  }
  .card {
    position: absolute;
    width: 540px;
    height: 309px;
    border-radius: 16px;
    box-shadow: 0 10px 30px rgba(0,0,0,.5);
    overflow: hidden;
  }
  .card--back {
    left: 60px;
    top: 120px;
    background: var(--card-dark);
  }
  .card--front {
    left: 600px;
    top: 440px;
    background: var(--card-light);
    color: var(--ink);
  }
  .brand {
    position: absolute;
    display: flex;
    align-items: center;
    gap: 16px;
    font-weight: 700;
    letter-spacing: -0.5px;
  }
  .brand__dot {
    width: 26px;
    height: 26px;
    border-radius: 50%;
    background: var(--neon);
  }
  .brand__divider {
    width: 1px;
    height: 52px;
    background: currentColor;
    opacity: .6;
  }
  .card--back .brand {
    left: 0; right: 0;
    top: 104px;
    justify-content: center;
    color: var(--white);
    font-size: 34px;
  }
  .tagline {
    position: absolute;
    left: 0; right: 0;
    bottom: 46px;
    margin: 0;
    text-align: center;
    color: var(--neon);
    font-size: 12px;
    font-weight: 700;
    letter-spacing: 3px;
    text-transform: uppercase;
  }
  .tagline__mark { color: var(--silver); letter-spacing: 0; }
  .card--front .brand {
    left: 0; right: 0;
    top: 32px;
    justify-content: center;
    color: var(--ink);
    font-size: 30px;
  }
  .rule {
    position: absolute;
    height: 2px;
    background: var(--rule);
  }
  .rule--address { left: 250px; right: 26px; top: 118px; }
  .rule--name { left: 168px; width: 150px; top: 184px; }
  .address {
    position: absolute;
    right: 26px;
    top: 128px;
    font-size: 11.5px;
    font-weight: 700;
  }
  .hours {
    position: absolute;
    right: 26px;
    top: 150px;
    text-align: right;
    font-size: 11.5px;
    line-height: 16px;
    font-weight: 700;
  }
  .hours__day {
    color: var(--neon);
    text-decoration: underline;
  }
  .hours__closed { color: var(--neon); }
  .person {
    position: absolute;
    left: 30px;
    top: 166px;
  }
  .person__name {
    color: var(--neon);
    font-size: 20px;
    font-weight: 900;
    margin: 0;
  }
  .person__role {
    font-size: 14px;
    color: var(--ink-soft);
    margin: 2px 0 0;
  }
  .contacts {
    position: absolute;
    left: 30px;
    top: 214px;
    margin: 0;
    padding: 0;
    list-style: none;
    font-size: 12.5px;
    font-weight: 700;
  }
  .contacts li {
    display: flex;
    align-items: center;
    gap: 10px;
    height: 20px;
  }
  .contacts svg { width: 16px; height: 16px; fill: var(--neon); flex: none; }
</style>
</head>
<body>

<section class="card card--back" aria-label="Card back">
  <div class="brand"><span class="brand__dot"></span><span class="brand__divider"></span><span>Hal's Remedies</span></div>
  <p class="tagline"><span class="tagline__mark">“</span> Where patients come first <span class="tagline__mark">”</span></p>
</section>

<section class="card card--front" aria-label="Card front">
  <div class="brand"><span class="brand__dot"></span><span class="brand__divider"></span><span>Hal's Remedies</span></div>

  <div class="rule rule--address"></div>
  <div class="address">7163 N Birch Rd Sioux Falls, SD 57291</div>
  <div class="hours">
    <div><span class="hours__day">Monday - Friday:</span> 8:00 a.m. - 7:00 p.m</div>
    <div><span class="hours__day">Saturday:</span> 8:00 a.m. - 12:00 p.m</div>
    <div class="hours__closed">Sunday: Closed</div>
  </div>

  <div class="person">
    <p class="person__name">Hal Norwick</p>
    <p class="person__role">Owner/Pharm D</p>
  </div>
  <div class="rule rule--name"></div>

  <ul class="contacts">
    <li>
      <svg viewBox="0 0 16 16" aria-hidden="true"><path d="M4 0h8a1 1 0 0 1 1 1v14a1 1 0 0 1-1 1H4a1 1 0 0 1-1-1V1a1 1 0 0 1 1-1zm1 2v10h6V2zm3 11a1 1 0 1 0 0 2 1 1 0 0 0 0-2z"/></svg>
      605-318-6027
    </li>
    <li>
      <svg viewBox="0 0 16 16" aria-hidden="true"><path d="M4 1h8v4H4zM1 6h14a1 1 0 0 1 1 1v5h-3v3H3v-3H0V7a1 1 0 0 1 1-1zm4 5v3h6v-3z"/></svg>
      605-318-6031
    </li>
    <li>
      <svg viewBox="0 0 16 16" aria-hidden="true"><path d="M0 3h16v1L8 9 0 4zm0 2.5 8 5 8-5V13H0z"/></svg>
      hal@halsremedies.example
    </li>
    <li>
      <svg viewBox="0 0 16 16" aria-hidden="true"><path d="M8 0a8 8 0 1 0 0 16A8 8 0 0 0 8 0zm0 2a6 6 0 0 1 0 12A6 6 0 0 1 8 2zM2.5 7.2h11v1.6h-11zM7.2 2.2h1.6v11.6H7.2z"/></svg>
      www.halsremedies.example
    </li>
  </ul>
</section>

</body>
</html>
```